Insurance company needs a business card design

We need a business card design for a Massachusetts-based insurance company Veloria Insurance, LLC. We provide auto insurance to Hispanic (Spanish- or Portuguese-speaking) immigrants in the United States. We will give these business cards to auto dealers where such customers typically go to purchase vehicles. We will provide a solution to the dealers to provide easy insurance to the customers buying cars at their dealerships. Veloria is the Spanish word for protection.
Contact Information for Business Card
Name, Designation, Company Name, Address, Phone Number, Email, Website
Look and feel
Each slider illustrates characteristics of the customer's brand and the style your logo design should communicate.

```html
<!DOCTYPE html>
<html lang="en">
<head>
<meta charset="utf-8">
<title>Veloria Insurance — Business Card</title>
<link rel="stylesheet" href="https://fonts.googleapis.com/css2?family=Roboto:wght@400;500;700;900&display=swap">
<style>
  :root {
    --navy: #0b3f73;
    --orange: #e8761a;
    --paper: #f4f4f3;
    --ink: #3a3a3a;
    --backdrop: #e7e5e1;
  }
  * { box-sizing: border-box; margin: 0; padding: 0; }
  html, body { width: 1200px; height: 960px; overflow: hidden; }
  body {
    background: var(--backdrop);
    font-family: "Roboto", Arial, sans-serif;
    position: relative;
  }
  .card {
    position: absolute;
    width: 760px;
    height: 434px;
    left: 220px;
    box-shadow: 0 6px 18px rgba(0,0,0,0.12);
  }
  .card-front { top: 30px; background: var(--navy); }
  .card-back { top: 496px; background: var(--paper); }

  .brand {
    position: absolute;
    display: flex;
    align-items: center;
    gap: 18px;
    font-weight: 900;
    letter-spacing: 1px;
    text-transform: uppercase;
  }
  .brand-mark { display: block; background: var(--orange); }
  .card-front .brand {
    left: 50%; top: 50%;
    transform: translate(-50%, -50%);
    color: #ffffff;
    font-size: 50px;
  }
  .card-front .brand-mark { width: 64px; height: 64px; }
  .card-back .brand {
    left: 300px; top: 52px;
    color: var(--navy);
    font-size: 34px;
  }
  .card-back .brand-mark { width: 44px; height: 44px; }

  .rule {
    position: absolute;
    left: 340px; top: 150px;
    width: 370px; height: 2px;
    background: var(--orange);
  }
  .person { position: absolute; left: 70px; top: 205px; }
  .person-name {
    color: var(--navy);
    font-weight: 700;
    font-size: 30px;
    letter-spacing: 0.3px;
  }
  .person-role {
    color: var(--orange);
    font-size: 22px;
    margin-top: 2px;
  }
  .contacts { list-style: none; margin-top: 18px; }
  .contacts li {
    display: flex; align-items: center; gap: 12px;
    color: var(--ink);
    font-size: 21px;
    line-height: 32px;
  }
  .contacts svg { width: 18px; height: 18px; flex: none; }
  .address {
    position: absolute;
    right: 50px; top: 176px;
    text-align: right;
    color: var(--ink);
    font-size: 20px;
    line-height: 27px;
  }
  .address-company { color: var(--navy); }
</style>
</head>
<body>
  <section class="card card-front">
    <div class="brand"><span class="brand-mark"></span>Veloria Insurance</div>
  </section>

  <section class="card card-back">
    <div class="brand"><span class="brand-mark"></span>Veloria Insurance</div>
    <div class="rule"></div>

    <div class="person">
      <div class="person-name">MARCUS HOLLOWELL</div>
      <div class="person-role">Managing Director</div>
      <ul class="contacts">
        <li>
          <svg viewBox="0 0 24 24" aria-hidden="true"><path fill="#e8761a" d="M6.6 10.8a15.1 15.1 0 0 0 6.6 6.6l2.2-2.2c.3-.3.7-.4 1-.2 1.1.4 2.3.6 3.6.6.6 0 1 .4 1 1V20c0 .6-.4 1-1 1A17 17 0 0 1 3 4c0-.6.4-1 1-1h3.5c.6 0 1 .4 1 1 0 1.3.2 2.5.6 3.6.1.3 0 .7-.2 1z"/></svg>
          203-555-0172
        </li>
        <li>
          <svg viewBox="0 0 24 24" aria-hidden="true"><rect x="2" y="5" width="20" height="14" fill="#e8761a"/><path d="M2 5l10 8 10-8" fill="none" stroke="#f4f4f3" stroke-width="2"/></svg>
          info@veloriainsurance.com
        </li>
        <li>
          <svg viewBox="0 0 24 24" aria-hidden="true"><g fill="none" stroke="#e8761a" stroke-width="2"><circle cx="12" cy="12" r="9"/><ellipse cx="12" cy="12" rx="4" ry="9"/><path d="M3 12h18"/></g></svg>
          www.veloriainsurance.com
        </li>
      </ul>
    </div>

    <address class="address">
      <div class="address-company">Veloria Insurance, LLC</div>
      <div>48 Harbor View Lane</div>
      <div>Fairhaven, MA 02719</div>
    </address>
  </section>
</body>
</html>
```